Business Card Design Project

Hello
I want a Simple Business card that uses the company logo that is easily reasonable but looks professional as I am an IT Services company and would look to share these cards with prospective clients.
The details are:
Kelvo Ridge Solutions
14 Marlow Crescent
Birmingham
B7 4QT
Telephone 0845 271 6049
I would like my name Gareth Wilcombe and my title Director on the card.
Target Market(s)
IT Professionals
Industry/Entity Type
Business

```html
<!DOCTYPE html>
<html lang="en">
<head>
<meta charset="utf-8">
<title>Kelvo Ridge Solutions – Business Card</title>
<link href="https://fonts.googleapis.com/css2?family=Arimo:wght@400;700&display=swap" rel="stylesheet">
<style>
  :root {
    --backdrop: #1c1c1c;
    --card-light: #ffffff;
    --card-light-shade: #f1f1f1;
    --card-dark: #2b2b2b;
    --ink: #1f1f1f;
    --ink-soft: #4a4a4a;
    --leaf: #8cc63f;
    --leaf-pale: #dcedc4;
    --paper-text: #f4f4f4;
  }
  * { box-sizing: border-box; margin: 0; padding: 0; }
  html, body {
    width: 1200px;
    height: 900px;
    overflow: hidden;
    background: var(--backdrop);
    font-family: "Arimo", Arial, sans-serif;
  }
  .canvas {
    position: relative;
    width: 1200px;
    height: 900px;
  }
  .card {
    position: absolute;
    left: 320px;
    width: 560px;
    height: 320px;
    border-radius: 22px;
    overflow: hidden;
  }
  /* Front */
  .card-front {
    top: 110px;
    background: linear-gradient(135deg, var(--card-light) 55%, var(--card-light-shade));
    color: var(--ink);
  }
  .front-decoration {
    position: absolute;
    right: -40px;
    top: -30px;
    width: 300px;
    height: 300px;
  }
  .brand-front {
    position: absolute;
    left: 40px;
    top: 64px;
    display: flex;
    align-items: center;
    gap: 12px;
  }
  .brand-dot {
    width: 26px;
    height: 26px;
    border-radius: 50%;
    background: var(--leaf);
    flex: none;
  }
  .brand-name {
    font-weight: 700;
    font-size: 40px;
    letter-spacing: -0.5px;
    line-height: 1;
  }
  .brand-front .brand-name { color: var(--ink); }
  .person {
    position: absolute;
    left: 40px;
    top: 176px;
    font-size: 21px;
    font-weight: 700;
    color: var(--ink);
  }
  .person .role {
    font-weight: 400;
    font-size: 15px;
    color: var(--ink-soft);
  }
  .contact {
    position: absolute;
    left: 40px;
    top: 220px;
    list-style: none;
    font-size: 15px;
    line-height: 1.55;
    color: var(--ink-soft);
  }
  .contact .label {
    color: var(--leaf);
    font-weight: 700;
    margin-right: 4px;
  }
  .address {
    position: absolute;
    left: 380px;
    top: 96px;
    font-style: normal;
    font-size: 14px;
    line-height: 1.4;
    color: var(--ink-soft);
  }
  .address .company { font-weight: 700; color: var(--ink); }
  .address .company-accent { color: var(--leaf); }

  /* Back */
  .card-back {
    top: 470px;
    background: var(--card-dark);
    display: flex;
    flex-direction: column;
    align-items: center;
    justify-content: center;
    gap: 30px;
  }
  .brand-back {
    display: flex;
    align-items: center;
    gap: 14px;
  }
  .brand-back .brand-name {
    color: var(--paper-text);
    font-size: 46px;
  }
  .website {
    font-size: 15px;
    color: var(--paper-text);
    letter-spacing: 0.3px;
  }
  .website .accent { color: var(--leaf); }
</style>
</head>
<body>
<main class="canvas">
  <section class="card card-front" aria-label="Business card front">
    <svg class="front-decoration" viewBox="0 0 300 300" aria-hidden="true">
      <circle cx="150" cy="150" r="130" fill="var(--leaf-pale)" opacity="0.55"/>
    </svg>
    <div class="brand-front">
      <span class="brand-dot"></span>
      <span class="brand-name">kelvo ridge</span>
    </div>
    <p class="person">Gareth Wilcombe, <span class="role">Director</span></p>
    <ul class="contact">
      <li><span class="label">T:</span>0845 271 6049</li>
      <li><span class="label">E:</span>gareth@kelvoridge.co.uk</li>
    </ul>
    <address class="address">
      <span class="company"><span class="company-accent">Kelvo Ridge</span> Solutions</span><br>
      14 Marlow Crescent<br>
      Birmingham<br>
      B7 4QT
    </address>
  </section>

  <section class="card card-back" aria-label="Business card back">
    <div class="brand-back">
      <span class="brand-dot"></span>
      <span class="brand-name">kelvo ridge</span>
    </div>
    <p class="website">www.<span class="accent">kelvoridge</span>solutions.com</p>
  </section>
</main>
</body>
</html>
```